Gelato Business Card

create a new business card using existing logo

Target Market(s)

B2B

Contact Information for Business Card

typical contact info: logo, address, email, phone, rep name

Colors
0355a3
33a6d7

Requirements
Must have
• a feel of high quality, luxury, happiness
• use cool, comforting color and texture of business card.
Nice to have
• "A Little Perfection Goes A Long Way!" TM
• or, "more quality, more flavor"
• or, "Flavor Matters"

```html
<!DOCTYPE html>
<html lang="en">
<head>
<meta charset="utf-8">
<title>Bellavita Artisan Gelato — Business Card</title>
<link href="https://fonts.googleapis.com/css2?family=Lato:wght@400;700&display=swap" rel="stylesheet">
<style>
  :root {
    --ink-blue: #3c46a6;
    --royal: #3a44a8;
    --sky: #33a6d7;
    --text-grey: #6b6b72;
    --card: #ffffff;
    --page: #ecebe8;
  }
  html, body {
    margin: 0;
    width: 1200px;
    height: 1023px;
    overflow: hidden;
    background: var(--page);
    font-family: "Lato", sans-serif;
  }
  .card {
    position: absolute;
    left: 100px;
    top: 226px;
    width: 1000px;
    height: 572px;
    background: var(--card);
    border-radius: 22px;
    overflow: hidden;
    box-shadow: 0 10px 30px rgba(0,0,0,0.18);
  }
  .card-swoosh {
    position: absolute;
    inset: 0;
    width: 100%;
    height: 100%;
  }
  .brand {
    position: absolute;
    left: 70px;
    top: 250px;
    display: flex;
    align-items: center;
    gap: 14px;
  }
  .brand-dot {
    width: 18px;
    height: 18px;
    border-radius: 50%;
    background: var(--sky);
    flex: none;
  }
  .brand-name {
    font-weight: 700;
    font-size: 30px;
    color: var(--ink-blue);
    letter-spacing: 1px;
    line-height: 1.15;
  }
  .contact {
    position: absolute;
    left: 470px;
    top: 80px;
    padding: 24px 0 30px 28px;
    border-left: 1.5px solid var(--ink-blue);
  }
  .rep-name {
    margin: 0;
    font-weight: 700;
    font-size: 34px;
    line-height: 1.2;
    letter-spacing: 1px;
    color: var(--ink-blue);
  }
  .rep-title {
    margin: 4px 0 22px;
    font-size: 19px;
    color: var(--text-grey);
  }
  .address {
    margin: 0 0 18px;
    font-size: 17px;
    line-height: 1.45;
    color: var(--text-grey);
  }
  .contact-list {
    list-style: none;
    margin: 0;
    padding: 0;
    font-size: 17px;
    line-height: 1.5;
    color: var(--text-grey);
  }
  .contact-list li {
    display: flex;
    align-items: center;
    gap: 11px;
  }
  .contact-list svg {
    width: 14px;
    height: 14px;
    flex: none;
  }
</style>
</head>
<body>
  <section class="card">
    <svg class="card-swoosh" viewBox="0 0 1000 572" preserveAspectRatio="none" aria-hidden="true">
      <defs>
        <linearGradient id="bandFill" x1="0" y1="1" x2="1" y2="0">
          <stop offset="0" stop-color="#8d94d6"/>
          <stop offset="0.35" stop-color="#3a44a8"/>
          <stop offset="1" stop-color="#3a44a8"/>
        </linearGradient>
      </defs>
      <path d="M370 572 C 770 500, 975 320, 1000 40 L1000 572 Z" fill="url(#bandFill)"/>
      <path d="M335 572 C 740 505, 955 330, 1000 15" fill="none" stroke="#ffffff" stroke-width="10"/>
      <path d="M300 572 C 700 510, 930 350, 985 0" fill="none" stroke="var(--sky)" stroke-width="5"/>
    </svg>

    <div class="brand">
      <span class="brand-dot"></span>
      <span class="brand-name">Bellavita<br>Artisan Gelato</span>
    </div>

    <div class="contact">
      <h1 class="rep-name">DANIEL REYES</h1>
      <p class="rep-title">Director</p>
      <p class="address">2480 Harbor Way, Suite 12<br>Larkspur, CA 94939 United States</p>
      <ul class="contact-list">
        <li>
          <svg viewBox="0 0 16 16"><path d="M4 1 L6.5 4 L5 6 C6 8.5 7.5 10 10 11 L12 9.5 L15 12 L13 15 C7 14.5 1.5 9 1 3 Z" fill="var(--ink-blue)"/></svg>
          (415) 555-0142
        </li>
        <li>
          <svg viewBox="0 0 16 16"><rect x="2" y="2" width="12" height="12" rx="2" fill="var(--ink-blue)"/><rect x="4.5" y="4.5" width="7" height="3" fill="#fff"/></svg>
          (415) 555-0178
        </li>
        <li>
          <svg viewBox="0 0 16 16"><rect x="1.5" y="3.5" width="13" height="9" fill="none" stroke="var(--ink-blue)" stroke-width="1.5"/><path d="M1.5 3.5 L8 9 L14.5 3.5" fill="none" stroke="var(--ink-blue)" stroke-width="1.5"/></svg>
          hello@bellavitagelato.com
        </li>
        <li>
          <svg viewBox="0 0 16 16"><circle cx="8" cy="8" r="6.5" fill="none" stroke="var(--ink-blue)" stroke-width="1.5"/><ellipse cx="8" cy="8" rx="2.8" ry="6.5" fill="none" stroke="var(--ink-blue)" stroke-width="1.2"/><path d="M1.5 8 H14.5" stroke="var(--ink-blue)" stroke-width="1.2"/></svg>
          www.bellavitagelato.com
        </li>
      </ul>
    </div>
  </section>
</body>
</html>
```